Cake website needs a professional WordPress design makeover!

I need a wordpress design for my company called Velvet Crumbhouse. It's a home cake business and I specialise in everything from cupcakes, celebratory cakes to couture wedding cakes. I have an existing one page wordpress website www.velvetcrumbhouse.example but it doesn't quite communicate elegance or showcase my skills so it desperately needs a complete change.

I purchased this theme
http://lumatheme.example/demos/themes/?product=vela
I basically want my website to look EXACTLY like this. I would obviously provide pictures of my work. I like the positioning of the pictures and texts and how each section are divided with the pictures. I also like the pop up of the welcome text on the home page. I would like that to say Welcome Velvet Crumbhouse.

One element I would like to keep from my original website are the slides on the home page. But will have a different caption with each slide. I will provide the three pictures for these slides.

The page format should be as follows:

Home
Discover Our Story
Tasteful Delights (Picture)
Discover Our Cakes - Clickable link below description going to the full cake menu with prices
The Perfect Blend (Picture)
Our Promise
Discover Your Special Day (Picture)
Wedding Cakes
Make an Order (Picture)
Get in touch

The menu on top of the page should read
Home, Our story, Our Cakes, Price List, Wedding cakes, Get in Touch

I would like to see the page of the full cake menu with the prices.
Signature colours Black, White and Pink

Target Market(s)

My main audience is targeted at women.

Industry/Entity Type

Wedding

Requirements
Must have
• Must look like the link I provided. Please use this as reference.
Nice to have
• Nice to see aspects of my logo, example the butterflies or the paisley design be subtly used around the website.

```html
<!DOCTYPE html>
<html lang="en">
<head>
<meta charset="utf-8">
<title>Velvet Crumbhouse</title>
<link href="https://fonts.googleapis.com/css2?family=Great+Vibes&family=Lato:wght@400;700;900&family=Open+Sans:wght@400;600&display=swap" rel="stylesheet">
<style>
:root{
  --pink:#e0457b;
  --pink-soft:#f4a6c2;
  --plum:#4e1530;
  --plum-deep:#35091f;
  --ink:#1c1c1c;
  --grey:#6d6d6d;
  --line:#e4e4e4;
  --white:#ffffff;
  --script:"Great Vibes", cursive;
  --head:"Lato", sans-serif;
  --body:"Open Sans", sans-serif;
}
*{box-sizing:border-box;margin:0;padding:0}
html,body{width:1200px;height:4528px;overflow:hidden}
body{background:var(--white);font-family:var(--body);color:var(--ink);position:relative}
section,header,footer{position:absolute;left:0;width:1200px}

/* header */
.site-header{top:0;height:75px;background:var(--white);border-bottom:1px solid var(--line)}
.brand{position:absolute;left:40px;top:20px;display:flex;align-items:center;gap:10px}
.brand-dot{width:14px;height:14px;border-radius:50%;background:var(--pink)}
.brand-name{font-family:var(--head);font-weight:700;font-size:20px;color:var(--plum)}
.top-bar{position:absolute;right:40px;top:8px;display:flex;align-items:center;gap:8px;font-size:11px;color:var(--pink)}
.top-bar .phone{margin-right:12px}
.social-dot{width:16px;height:16px;border-radius:50%;background:var(--pink)}
.main-nav{position:absolute;right:40px;top:38px;display:flex;gap:8px;font-family:var(--head);font-size:13px}
.main-nav a{color:var(--ink);text-decoration:none;padding:5px 12px;border-radius:14px}
.main-nav a.active{background:var(--pink);color:var(--white)}

/* hero */
.hero{top:75px;height:453px;background:linear-gradient(100deg,var(--plum-deep),#6a2146 55%,#8a3a60);overflow:hidden}
.hero-photo{position:absolute;right:0;top:0;width:520px;height:453px;background:linear-gradient(90deg,rgba(138,58,96,0),rgba(214,128,166,.55) 40%,rgba(236,170,198,.6) 70%,rgba(138,58,96,.3))}
.hero-text{position:absolute;left:160px;top:95px;width:560px;color:var(--white)}
.hero-text .script{font-family:var(--script);font-size:70px;color:var(--pink-soft);line-height:1}
.hero-text h1{font-family:var(--script);font-size:82px;font-weight:400;color:var(--pink);line-height:1;margin-top:-8px}
.hero-text p{font-family:var(--script);font-size:25px;line-height:1.25;margin-top:14px;color:#f4dbe6}
.btn{display:inline-block;background:var(--pink);color:var(--white);font-family:var(--head);font-weight:700;font-size:12px;letter-spacing:.08em;padding:9px 20px;border-radius:18px;text-decoration:none}
.hero .btn{margin-top:24px}
.dots{position:absolute;left:50%;bottom:18px;transform:translateX(-50%);display:flex;gap:8px}
.dots i{width:8px;height:8px;border-radius:50%;background:rgba(255,255,255,.45)}
.dots i.on{background:var(--white)}

/* content sections */
.content{background:var(--white)}
.copy{position:absolute;width:460px}
.copy .script{font-family:var(--script);font-size:60px;color:var(--pink);line-height:.9}
.copy h2{font-family:var(--head);font-weight:900;font-size:44px;letter-spacing:.02em;line-height:1;margin:2px 0 22px}
.copy p{font-size:13px;line-height:1.75;color:var(--grey);margin-bottom:14px}
.copy strong{color:var(--ink);font-weight:600}

.cluster{position:absolute;width:424px;height:424px}
.diamond{position:absolute;width:150px;height:150px;transform:rotate(45deg);border:5px solid var(--white);box-shadow:0 0 0 1px #f1e4ea}
.diamond.t{left:137px;top:31px}
.diamond.l{left:31px;top:137px}
.diamond.r{left:243px;top:137px}
.diamond.b{left:137px;top:243px}
.g1{background:linear-gradient(135deg,#f7c6d9,#e8628f)}
.g2{background:linear-gradient(135deg,#bfe9f1,#4fb7d4)}
.g3{background:linear-gradient(135deg,#f9e2c6,#d99a6a)}
.g4{background:linear-gradient(135deg,#fbd4e2,#c73d72)}
.g5{background:linear-gradient(135deg,#fff3d9,#f2b6c9)}

/* photo bands */
.band{overflow:hidden}
.band-photo{position:absolute;inset:0}
.band-badge{position:absolute;left:50%;top:50%;width:200px;height:200px;margin:-100px 0 0 -100px;border-radius:50%;background:rgba(255,255,255,.9);text-align:center;padding-top:46px}
.band-badge .script{font-family:var(--script);font-size:48px;color:var(--pink);line-height:.9}
.band-badge .word{font-family:var(--head);font-weight:900;font-size:30px;line-height:1.05;color:var(--ink)}
.band-badge svg{display:block;margin:10px auto 0}
.band-badge.three{padding-top:30px}
.band-badge.three .word{font-size:27px}

/* contact */
.contact-head{position:absolute;left:0;width:1200px;top:28px;text-align:center}
.contact-head .script{font-family:var(--script);font-size:60px;color:var(--pink);line-height:.9}
.contact-head h2{font-family:var(--head);font-weight:900;font-size:40px;line-height:1.1}
.contact-info{position:absolute;left:150px;top:150px;width:360px}
.info-row{display:flex;gap:16px;margin-bottom:14px}
.info-row svg{flex:none}
.info-row h4{font-family:var(--head);font-size:13px;color:var(--pink);margin-bottom:2px}
.info-row p{font-size:12px;color:var(--grey);line-height:1.5}
.contact-form{position:absolute;left:610px;top:145px;width:440px}
.field{border:1px solid var(--line);height:32px;font-size:11px;color:#9a9a9a;padding:9px 12px;margin-bottom:10px;font-family:var(--body)}
.field-row{display:flex;gap:12px}
.field-row .field{flex:1}
.field.msg{height:60px}
.contact-form .btn{display:block;width:100%;text-align:center;border-radius:3px;padding:10px}

/* footer */
.site-footer{top:4341px;height:187px;background:var(--plum)}
.footer-social{position:absolute;top:40px;left:0;width:1200px;display:flex;justify-content:center;gap:14px}
.footer-social i{width:38px;height:38px;border-radius:50%;background:var(--pink)}
.footer-bar{position:absolute;bottom:0;left:0;width:1200px;height:68px;background:var(--plum-deep);padding:16px 40px;color:#d9b8c7;font-size:11px}
.footer-bar nav{display:flex;gap:22px;margin-bottom:8px;font-family:var(--head)}
.footer-bar nav a{color:var(--white);text-decoration:none}
</style>
</head>
<body>

<header class="site-header">
  <div class="brand"><span class="brand-dot"></span><span class="brand-name">Velvet Crumbhouse</span></div>
  <div class="top-bar">
    <span class="phone">+1 555 014 2288</span>
    <span class="social-dot"></span><span class="social-dot"></span><span class="social-dot"></span><span class="social-dot"></span>
  </div>
  <nav class="main-nav">
    <a class="active" href="#">Home</a><a href="#">Our Story</a><a href="#">Our Cakes</a><a href="#">Price List</a><a href="#">Wedding Cakes</a><a href="#">Get In Touch</a>
  </nav>
</header>

<section class="hero">
  <div class="hero-photo" role="img" aria-label="Photo of a pink swirl-frosted cupcake"></div>
  <div class="hero-text">
    <div class="script">Welcome</div>
    <h1>Velvet Crumbhouse</h1>
    <p>There are many variations of passages of Lorem Ipsum available, but the majority have suffered alteration in some form, by injected humour, or randomised words.</p>
    <a class="btn" href="#">SEE OUR CAKES</a>
  </div>
  <div class="dots"><i class="on"></i><i></i><i></i></div>
</section>

<section class="content story" style="top:528px;height:462px">
  <div class="copy" style="left:150px;top:60px">
    <div class="script">Discover</div>
    <h2>OUR STORY</h2>
    <p>Founded in 2012 in a small home kitchen, Velvet Crumbhouse began with a love of baking and a wish to make every celebration feel special. Each cake is made by hand, using fresh butter, free-range eggs and flavours chosen with care for the moment it marks.</p>
    <a class="btn" href="#">ABOUT US</a>
  </div>
  <div class="cluster" style="left:660px;top:20px">
    <div class="diamond t g2" role="img" aria-label="Photo of blue frosted cupcakes"></div>
    <div class="diamond l g1" role="img" aria-label="Photo of pink cupcakes"></div>
    <div class="diamond r g3" role="img" aria-label="Photo of cupcakes with sprinkles"></div>
    <div class="diamond b g4" role="img" aria-label="Photo of a rose-topped cupcake"></div>
  </div>
</section>

<section class="band" style="top:990px;height:324px">
  <div class="band-photo" role="img" aria-label="Photo of a slice of layered cake on a dessert table" style="background:linear-gradient(90deg,#d9c3b4,#f2e6dc 35%,#c9a08a 60%,#7b2b36)"></div>
  <div class="band-badge"><div class="script">Tasteful</div><div class="word">DELIGHTS</div>
    <svg width="14" height="14" viewBox="0 0 14 14"><circle cx="7" cy="7" r="6" fill="none" stroke="#1c1c1c"/><path d="M4 6l3 3 3-3" fill="none" stroke="#1c1c1c"/></svg></div>
</section>

<section class="content cakes" style="top:1314px;height:623px">
  <div class="cluster" style="left:120px;top:40px">
    <div class="diamond t g5" role="img" aria-label="Photo of a cupcake with a sugar flower"></div>
    <div class="diamond l g1" role="img" aria-label="Photo of pink cupcakes"></div>
    <div class="diamond r g4" role="img" aria-label="Photo of cupcakes with pink icing"></div>
    <div class="diamond b g2" role="img" aria-label="Photo of turquoise cupcakes"></div>
  </div>
  <div class="copy" style="left:610px;top:60px">
    <div class="script">Discover</div>
    <h2>OUR CAKES</h2>
    <p>Velvet Crumbhouse offers a wide range of cakes and cupcakes made using the finest ingredients. We specialise in everything from cupcakes and celebratory cakes to couture wedding cakes, each designed to suit your taste and occasion.</p>
    <p>Every bake is finished by hand, whether it is a simple sponge for a family tea or a tiered centrepiece for a grand party, and all flavours can be tailored to you.</p>
    <p>Looking for something more than the menu? Talk to us about bespoke designs, colour palettes and gift boxes made for birthdays, showers and anniversaries.</p>
    <a class="btn" href="#">VIEW THE FULL CAKE MENU</a>
  </div>
</section>

<section class="band" style="top:1937px;height:373px">
  <div class="band-photo" role="img" aria-label="Photo of a row of colourful frosted cupcakes" style="background:linear-gradient(90deg,#7cc7c8,#e8a6c1 30%,#c8d67c 55%,#4da7c6 80%,#f0b8cc)"></div>
  <div class="band-badge"><div class="script">The Perfect</div><div class="word">BLEND</div>
    <svg width="14" height="14" viewBox="0 0 14 14"><circle cx="7" cy="7" r="6" fill="none" stroke="#1c1c1c"/><path d="M4 6l3 3 3-3" fill="none" stroke="#1c1c1c"/></svg></div>
</section>

<section class="content promise" style="top:2310px;height:438px">
  <div class="copy" style="left:150px;top:60px">
    <div class="script">Discover</div>
    <h2>OUR PROMISE</h2>
    <p>Every order is baked fresh for the day it is needed, never frozen, and decorated with the same care we would give our own family. We listen closely, answer quickly and deliver on time, so you can simply enjoy the celebration.</p>
    <a class="btn" href="#">OUR PROMISE</a>
  </div>
  <div class="cluster" style="left:660px;top:10px">
    <div class="diamond t g5" role="img" aria-label="Photo of a cupcake with a heart decoration"></div>
    <div class="diamond l g1" role="img" aria-label="Photo of pink iced cupcakes"></div>
    <div class="diamond r g4" role="img" aria-label="Photo of a heart-topped cupcake"></div>
    <div class="diamond b g3" role="img" aria-label="Photo of vanilla cupcakes"></div>
  </div>
</section>

<section class="band" style="top:2748px;height:434px">
  <div class="band-photo" role="img" aria-label="Photo of cupcakes seen from above in bright colours" style="background:linear-gradient(120deg,#f3d04a,#e86a9a 25%,#8bd0e0 45%,#f1a2c4 65%,#b7dc6e 85%,#f5e6a0)"></div>
  <div class="band-badge three"><div class="script">Discover</div><div class="word">YOUR<br>SPECIAL<br>DAY</div></div>
</section>

<section class="content wedding" style="top:3182px;height:385px">
  <div class="cluster" style="left:120px;top:-20px">
    <div class="diamond t g3" role="img" aria-label="Photo of a tiered wedding cake"></div>
    <div class="diamond l g5" role="img" aria-label="Photo of white wedding cupcakes"></div>
    <div class="diamond r g1" role="img" aria-label="Photo of pink rose cupcakes"></div>
    <div class="diamond b g4" role="img" aria-label="Photo of a cake with sugar roses"></div>
  </div>
  <div class="copy" style="left:610px;top:40px">
    <div class="script">Discover</div>
    <h2>WEDDING CAKES</h2>
    <p><strong>Velvet Crumbhouse would be delighted to be part of your wedding celebration.</strong></p>
    <p>We love to work with each couple to create a cake that reflects your style, theme and flowers, from elegant tiers to towers of cupcakes.</p>
    <p>Consultations are held in a relaxed setting with tasting boxes so you can choose flavours together. Please get in touch to book an appointment.</p>
  </div>
</section>

<section class="band" style="top:3567px;height:427px">
  <div class="band-photo" role="img" aria-label="Photo of cupcakes with cinnamon sticks on a wooden table" style="background:linear-gradient(90deg,#caa07c,#f2dccd 35%,#a9643d 65%,#5b2a1a)"></div>
  <div class="band-badge"><div class="script">Make</div><div class="word">AN ORDER</div>
    <svg width="14" height="14" viewBox="0 0 14 14"><circle cx="7" cy="7" r="6" fill="none" stroke="#1c1c1c"/><path d="M4 6l3 3 3-3" fill="none" stroke="#1c1c1c"/></svg></div>
</section>

<section class="content contact" style="top:3994px;height:347px">
  <div class="contact-head"><div class="script">Get</div><h2>IN TOUCH</h2></div>
  <div class="contact-info">
    <div class="info-row">
      <svg width="22" height="26" viewBox="0 0 22 26"><path d="M11 1a8 8 0 0 0-8 8c0 6 8 15 8 15s8-9 8-15a8 8 0 0 0-8-8z" fill="#e0457b"/><circle cx="11" cy="9" r="3" fill="#fff"/></svg>
      <div><h4>Address</h4><p>18 Larkspur Lane, Ashby Vale<br>Open by appointment only</p></div>
    </div>
    <div class="info-row">
      <svg width="22" height="22" viewBox="0 0 22 22"><path d="M5 2l4 4-2 3c1 3 3 5 6 6l3-2 4 4-3 3C9 20 2 13 2 5z" fill="#e0457b"/></svg>
      <div><h4>Call us</h4><p>+1 555 014 2288</p></div>
    </div>
    <div class="info-row">
      <svg width="22" height="18" viewBox="0 0 22 18"><rect x="1" y="2" width="20" height="14" rx="2" fill="#e0457b"/><path d="M2 4l9 7 9-7" fill="none" stroke="#fff" stroke-width="1.5"/></svg>
      <div><h4>Email us</h4><p>hello@velvetcrumbhouse.example</p></div>
    </div>
  </div>
  <form class="contact-form">
    <div class="field-row"><div class="field">First Name</div><div class="field">Last Name</div></div>
    <div class="field">Email</div>
    <div class="field msg">Message</div>
    <a class="btn" href="#">SEND MESSAGE</a>
  </form>
</section>

<footer class="site-footer">
  <div class="footer-social"><i></i><i></i><i></i><i></i></div>
  <div class="footer-bar">
    <nav><a href="#">Home</a><a href="#">Our Story</a><a href="#">Our Cakes</a><a href="#">Price List</a><a href="#">Wedding Cakes</a><a href="#">Get In Touch</a></nav>
    <div>Copyright © Velvet Crumbhouse 2016. All Rights Reserved.</div>
  </div>
</footer>

</body>
</html>
```